Business card for my new company (Accounting firm)

I need a business card for my new business Corvane Advisory and Ledger SA. Our services are accounting, tax, audit and financial management. Our customers are small companies, start-ups and new companies. The final design has to show financial security, trust and growth. Please find our logo attached to the business card. Text for the business card: Corvane Advisory and Ledger SA Tomas da Varela Director and Founder Certified Accountant Tel. 022 418 27 35 tv@corvaneconseil.ch www.corvaneconseil.ch Rue des Vergers-Bleus 14 1201 Geneva
Target Market(s)
Our customers are small companies, start-ups and new companies.
Industry/Entity Type
Finance And Accounting
Contact Information for Business Card
Corvane Conseil et Registre SA
Tomas da Varela
Directeur et Fondateur
Expert-comptable diplômé
Tél. 022 418 27 35
tv@corvaneconseil.ch
www.corvaneconseil.ch
Rue des Vergers-Bleus 14
1201 Genève

```html
<!DOCTYPE html>
<html lang="fr">
<head>
<meta charset="utf-8">
<title>Corvane Conseil et Registre SA – Carte de visite</title>
<link rel="stylesheet" href="https://fonts.googleapis.com/css2?family=Saira:wght@400;600;700&display=swap">
<style>
  :root {
    --page-bg: #e6e8eb;
    --navy: #1b5a8f;
    --blue: #2a74ad;
    --mid-blue: #3a8fcf;
    --sky: #3fb0e6;
    --accent-name: #2ba6df;
    --ink: #4a4d52;
    --ink-soft: #5c6066;
    --rule: #8a8d92;
    --white: #ffffff;
  }
  * { margin: 0; padding: 0; box-sizing: border-box; }
  html, body {
    width: 1200px; height: 1000px; overflow: hidden;
    background: var(--page-bg);
    font-family: "Saira", Arial, sans-serif;
  }
  .canvas { position: relative; width: 1200px; height: 1000px; }

  .card {
    position: absolute;
    width: 760px; height: 434px;
    border-radius: 4px;
    box-shadow: 0 10px 28px rgba(0,0,0,.18);
    overflow: hidden;
  }

  /* Front */
  .card-front {
    left: 100px; top: 50px;
    background: linear-gradient(135deg, var(--navy) 0%, var(--blue) 60%, #3a84bd 100%);
  }
  .card-front .wordmark {
    position: absolute; right: 70px; top: 170px;
    display: flex; align-items: center; gap: 18px;
  }
  .card-front .wordmark-square {
    width: 46px; height: 46px; background: var(--white);
  }
  .card-front .wordmark-name {
    color: var(--white); font-weight: 600; font-size: 34px;
    letter-spacing: 2px; line-height: 1.1;
  }

  /* Back */
  .card-back {
    left: 340px; top: 516px;
    background: var(--white);
  }
  .card-back .wordmark {
    position: absolute; left: 56px; top: 120px; width: 280px;
    display: flex; flex-direction: column; align-items: center; gap: 16px;
  }
  .card-back .wordmark-square {
    width: 64px; height: 64px; background: var(--mid-blue);
  }
  .card-back .wordmark-name {
    color: var(--ink); font-weight: 600; font-size: 26px;
    letter-spacing: 1.5px; text-align: center; line-height: 1.15;
  }
  .divider {
    position: absolute; left: 360px; top: 92px;
    width: 2px; height: 170px; background: var(--rule);
  }
  .contact {
    position: absolute; left: 392px; top: 92px;
    color: var(--ink-soft); font-size: 17px; line-height: 1.35;
  }
  .contact .person-name {
    color: var(--accent-name); font-weight: 700; font-size: 24px; line-height: 1.2;
  }
  .contact .details { margin-top: 18px; }

  .address {
    position: absolute; right: 172px; bottom: 54px;
    color: var(--ink); font-size: 19px; line-height: 1.2;
    white-space: nowrap; text-align: right;
  }
  .band { position: absolute; height: 14px; }
  .band-1 { left: 0; width: 330px; bottom: 0; background: var(--blue); }
  .band-2 { left: 340px; width: 250px; bottom: 30px; background: var(--mid-blue); }
  .band-3 { left: 600px; width: 160px; bottom: 60px; background: var(--sky); }
</style>
</head>
<body>
<div class="canvas">

  <section class="card card-front" aria-label="Recto">
    <div class="wordmark">
      <span class="wordmark-square"></span>
      <span class="wordmark-name">Corvane Conseil<br>et Registre</span>
    </div>
  </section>

  <section class="card card-back" aria-label="Verso">
    <div class="wordmark">
      <span class="wordmark-square"></span>
      <span class="wordmark-name">Corvane Conseil<br>et Registre</span>
    </div>

    <div class="divider"></div>

    <div class="contact">
      <p class="person-name">Tomas da Varela</p>
      <p>Directeur et Fondateur</p>
      <p>Expert-comptable diplômé</p>
      <div class="details">
        <p>022 418 27 35</p>
        <p>tv@corvaneconseil.ch</p>
        <p>www.corvaneconseil.ch</p>
      </div>
    </div>

    <p class="address">Rue des Vergers-Bleus 14, 1201 Genève</p>

    <span class="band band-1"></span>
    <span class="band band-2"></span>
    <span class="band band-3"></span>
  </section>

</div>
</body>
</html>
```